Korvane Sky Works, LLC - Business Card

I currently have a drone business that specializes in aerial photography, thermal image inspections, deer recovery, search and rescue, custom agricultural applications. i will attach my current business card as well as some logos to incorporate for a new up to date business card
Updates

Designs look the same

Sick

Target Market(s)

farmers, hunters

Contact Information for Business Card

name address phone number (as existing card i attached)

Requirements
Must have
• im good with existing business card, but would like an agricultural twist

```html
<!DOCTYPE html>
<html lang="en">
<head>
<meta charset="utf-8">
<title>Korvane Sky Works, LLC - Business Card</title>
<link rel="stylesheet" href="https://fonts.googleapis.com/css2?family=Mulish:wght@400;600;800&display=swap">
<style>
  :root {
    --field-green: #46923f;
    --leaf-green: #5aa84f;
    --paper: #ffffff;
    --ink: #111111;
    --backdrop: #3a3a3a;
  }
  * { margin: 0; padding: 0; box-sizing: border-box; }
  html, body { width: 1200px; height: 1059px; overflow: hidden; }
  body {
    background: var(--backdrop);
    font-family: "Mulish", sans-serif;
    position: relative;
  }
  .card {
    position: absolute;
    left: 255px;
    width: 690px;
    height: 392px;
    overflow: hidden;
  }
  .card-front { top: 100px; background: var(--paper); }
  .card-back { top: 537px; background: var(--field-green); }

  .wave-art { position: absolute; inset: 0; width: 690px; height: 392px; }

  .brand-mark {
    position: absolute;
    display: flex;
    align-items: center;
    gap: 10px;
    font-weight: 800;
    font-size: 32px;
  }
  .brand-mark .dot { width: 16px; height: 16px; border-radius: 50%; }
  .card-front .brand-mark { left: 58px; top: 132px; color: var(--field-green); }
  .card-front .brand-mark .dot { background: var(--field-green); }
  .card-back .brand-mark { left: 0; right: 0; top: 162px; justify-content: center; color: var(--paper); font-size: 40px; }
  .card-back .brand-mark .dot { background: var(--paper); width: 20px; height: 20px; }

  .holder { position: absolute; right: 41px; top: 50px; text-align: right; }
  .holder-name { color: var(--field-green); font-weight: 800; font-size: 26px; letter-spacing: 0.5px; line-height: 1.1; }
  .holder-role { color: var(--ink); font-size: 16px; margin-top: 4px; letter-spacing: 0.5px; }
  .side-tab {
    position: absolute; right: 0; top: 52px; width: 21px; height: 48px;
    background: var(--field-green); border-radius: 6px 0 0 6px;
  }
  .leaf-accent {
    position: absolute; left: 560px; top: 123px; width: 90px; height: 108px;
    border-radius: 50%;
    background: radial-gradient(circle, rgba(70,146,63,0.55), rgba(70,146,63,0) 70%);
  }

  .contact-list {
    position: absolute; right: 41px; top: 256px; list-style: none;
    color: var(--paper); font-size: 17px; text-align: right;
  }
  .contact-list li { display: flex; justify-content: flex-end; align-items: center; gap: 8px; height: 29.5px; }
  .contact-list svg { width: 13px; height: 13px; fill: var(--paper); flex: none; }

  .service-list {
    position: absolute; left: 0; right: 0; top: 318px;
    color: var(--paper); font-size: 17px; text-align: center; line-height: 27px;
  }
  .service-list p { display: flex; justify-content: center; gap: 10px; }
  .service-list span::before { content: "\2022"; margin-right: 7px; }
</style>
</head>
<body>

<section class="card card-front" aria-label="Business card front">
  <svg class="wave-art" viewBox="0 0 690 392" aria-hidden="true">
    <path d="M0,250 C60,320 190,345 300,300 C420,250 520,200 690,218 L690,392 L0,392 Z" fill="#46923f"/>
    <path d="M0,228 C40,300 150,318 276,275" fill="none" stroke="#111" stroke-width="9" stroke-linecap="round"/>
    <path d="M90,350 C220,395 380,300 600,192" fill="none" stroke="#fff" stroke-width="5" stroke-linecap="round"/>
  </svg>

  <div class="brand-mark"><span class="dot"></span>Korvane</div>

  <div class="holder">
    <p class="holder-name">DORIAN WELKE</p>
    <p class="holder-role">OWNER</p>
  </div>
  <div class="side-tab"></div>
  <div class="leaf-accent" role="img" aria-label="Decorative leaves with scattered dots"></div>

  <ul class="contact-list">
    <li>419-555-0142
      <svg viewBox="0 0 24 24"><path d="M6.6 10.8a15 15 0 0 0 6.6 6.6l2.2-2.2a1 1 0 0 1 1-.25 11.4 11.4 0 0 0 3.6.57 1 1 0 0 1 1 1V20a1 1 0 0 1-1 1A17 17 0 0 1 3 4a1 1 0 0 1 1-1h3.5a1 1 0 0 1 1 1c0 1.25.2 2.45.57 3.57a1 1 0 0 1-.25 1z"/></svg></li>
    <li>hello@korvanesky.com
      <svg viewBox="0 0 24 24"><path d="M2 5h20v14H2z M3 6l9 7 9-7" fill="none" stroke="#fff" stroke-width="2"/></svg></li>
    <li>www.korvanesky.com
      <svg viewBox="0 0 24 24"><circle cx="12" cy="12" r="10"/><path d="M2 12h20M12 2c3 3 3 17 0 20M12 2c-3 3-3 17 0 20" fill="none" stroke="#46923f" stroke-width="1.6"/></svg></li>
    <li>214 W. Orchard St. Brandt, OH 45390
      <svg viewBox="0 0 24 24"><path d="M12 2a7 7 0 0 0-7 7c0 5 7 13 7 13s7-8 7-13a7 7 0 0 0-7-7zm0 9.5A2.5 2.5 0 1 1 12 6.5a2.5 2.5 0 0 1 0 5z"/></svg></li>
  </ul>
</section>

<section class="card card-back" aria-label="Business card back">
  <div class="brand-mark"><span class="dot"></span>Korvane</div>
  <div class="service-list">
    <p><span>Thermal Image Inspections</span><span>Deer Recovery</span></p>
    <p><span>Search &amp; Rescue</span><span>Real Estate Photography</span></p>
  </div>
</section>

</body>
</html>
```